Harbourlight Campus Lodgings needs a business card design

Hi Guys,

We are a Student Accommodation company in Australia. We already have a logo which I will submit.

I will require the design of the business cards from you.

I am after something that looks clean, modern and that people feel interested and actually want to contact us.

We would like to see designs that are innovative.

On the business cards I will require to have:

Employee Name
Position
Phone number
Email
Facebook page

I hope you can help me with this project guys as I have heard really good things from you.

```html
<!DOCTYPE html>
<html lang="en">
<head>
<meta charset="utf-8">
<title>Harbourlight Campus Lodgings – Business Cards</title>
<link rel="stylesheet" href="https://fonts.googleapis.com/css2?family=Oswald:wght@600&family=Roboto:wght@400;500&display=swap">
<style>
  :root {
    --bg: #e9e6e1;
    --card: #ffffff;
    --yellow: #f0ab0a;
    --green: #0f9320;
    --green-dark: #1d5a22;
    --ink: #333333;
  }
  * { box-sizing: border-box; margin: 0; padding: 0; }
  html, body { width: 1200px; height: 905px; overflow: hidden; }
  body { background: var(--bg); position: relative; font-family: "Roboto", Arial, sans-serif; }

  .card {
    position: absolute;
    width: 520px; height: 296px;
    background: var(--card);
    box-shadow: 0 10px 24px rgba(0,0,0,0.18);
    overflow: hidden;
  }
  .card--front { left: 80px; top: 140px; }
  .card--back  { left: 600px; top: 450px; }

  .brand {
    position: absolute; left: 26px; top: 40px;
    display: flex; align-items: center; gap: 10px;
  }
  .brand__mark { width: 36px; height: 36px; background: var(--yellow); }
  .brand__name {
    font-family: "Oswald", "Arial Narrow", sans-serif; font-weight: 600;
    color: var(--green); font-size: 17px; line-height: 1.05; text-transform: uppercase;
  }

  .band {
    position: absolute; left: 0; right: 0; background: var(--yellow);
    color: #fff; display: flex; align-items: center; padding-left: 30px;
  }
  .card--front .band { top: 176px; height: 36px; }
  .card--back .band  { top: 142px; height: 44px; }

  .website { font-size: 11px; letter-spacing: 3px; }
  .address { font-size: 12px; }

  .slab { position: absolute; background: var(--green); clip-path: polygon(30px 0, 100% 0, 100% 100%, 0 100%); }
  .card--front .slab { left: 290px; right: 0; top: 128px; height: 90px; }
  .card--back .slab  { left: 300px; width: 208px; top: 70px; height: 130px; padding: 28px 0 0 50px; }

  .accent-strip { position: absolute; right: 0; width: 20px; top: 60px; height: 126px; background: var(--yellow); }

  .person__name {
    font-family: "Oswald", "Arial Narrow", sans-serif; font-weight: 600;
    font-size: 22px; color: var(--green-dark); text-transform: uppercase; line-height: 1;
  }
  .person__role { font-size: 9px; letter-spacing: 1px; color: var(--green-dark); text-transform: uppercase; margin-top: 4px; }

  .contacts { position: absolute; left: 26px; top: 206px; list-style: none; }
  .contacts li { display: flex; align-items: center; gap: 7px; font-size: 10px; color: var(--ink); height: 17px; }
  .contacts svg { width: 10px; height: 10px; fill: var(--ink); }
</style>
</head>
<body>
  <section class="card card--front" aria-label="Card front">
    <div class="brand">
      <span class="brand__mark"></span>
      <span class="brand__name">Harbourlight<br>Campus Lodgings</span>
    </div>
    <div class="band"><span class="website">www.harbourlight.example</span></div>
    <div class="slab"></div>
  </section>

  <section class="card card--back" aria-label="Card back">
    <div class="brand">
      <span class="brand__mark"></span>
      <span class="brand__name">Harbourlight<br>Campus Lodgings</span>
    </div>
    <div class="accent-strip"></div>
    <div class="band"><span class="address">42 Quayside Lane, Level 3, Harbour St.</span></div>
    <div class="slab">
      <div class="person__name">Mara Ellison</div>
      <div class="person__role">General Manager</div>
    </div>
    <ul class="contacts">
      <li><svg viewBox="0 0 10 10"><path d="M2 0.5h2l0.8 2.3-1.2 0.9a5 5 0 0 0 2.7 2.7l0.9-1.2 2.3 0.8v2a1.5 1.5 0 0 1-1.5 1.5A8 8 0 0 1 0.5 2 1.5 1.5 0 0 1 2 0.5z"/></svg>021 555 0147</li>
      <li><svg viewBox="0 0 10 10"><path d="M3 0h4a1 1 0 0 1 1 1v8a1 1 0 0 1-1 1H3a1 1 0 0 1-1-1V1a1 1 0 0 1 1-1zm0 1.5v6h4v-6z"/></svg>021 555 0148</li>
      <li><svg viewBox="0 0 10 10"><path d="M0 2h10v6H0zm1 1v0.3l4 2.5 4-2.5V3z"/></svg>mara@harbourlight.example</li>
      <li><svg viewBox="0 0 10 10"><circle cx="5" cy="5" r="4.5" fill="none" stroke="#333" stroke-width="1"/><path d="M0.5 5h9M5 0.5v9" stroke="#333" stroke-width="0.8"/></svg>www.harbourlight.example</li>
    </ul>
  </section>
</body>
</html>
```